Re-design of current business cards

We are updating our website with new colors and layout. Would like to re-design our business cards to co-ordinate. See attached pdf with new Brindlecraft website colors. We would also like to combine our 2 brands on the one business card. Attached is the new design for our Brindlecraft website, current business cards, which are one sided, brindlecraft logo in tiff, .ai for fonts. Brindlecraft logo font is Optimum, Quillmarsh website home page image, Quillmarsh brand statics for products which includes the logo for this brand.

Quillmarsh brand will stay the dark gray on the website. See attached statics for product and website home page.
Updates

The business cards will be 2 sided. Brindlecraft Brand on one side and Quillmarsh Brand on the other. The colors for Brindlecraft need to follow the color scheme of the brindlecraft website pdf I uploaded. The colors are a blue, lighter teal blue and white. Quillmarsh needs to follow the dark gray color on files uploaded

Target Market(s)

The trade and consumers

Industry/Entity Type

Home Furnishing

Contact Information for Business Card

We are updating our website with new colors and layout. Would like to re-design our business cards to co-ordinate. We would also like to combine our 2 brands onto 1 2 sided business cards.

Requirements
Must have
• Colors that match our new website, see attached image.
• RGB colors
• navy -#152842
• teal - 98aeb9
• The gray color used for Quillmarsh brands.
• ll logos and fonts should stay the same.

```html
<!DOCTYPE html>
<html lang="en">
<head>
<meta charset="utf-8">
<title>Brindlecraft &amp; Quillmarsh Business Cards</title>
<link rel="stylesheet" href="https://fonts.googleapis.com/css2?family=Marcellus&family=Open+Sans:wght@400;600&display=swap">
<style>
  :root {
    --stage: #2b2b2b;
    --quill-gray: #626262;
    --paper: #ffffff;
    --navy: #152842;
    --teal: #98aeb9;
    --ink: #152842;
    --rule: #c9d3d8;
  }
  * { margin: 0; padding: 0; box-sizing: border-box; }
  html, body { width: 1200px; height: 1200px; overflow: hidden; }
  body { background: var(--stage); position: relative; font-family: "Open Sans", sans-serif; }

  .card {
    position: absolute;
    width: 620px;
    height: 354px;
    border-radius: 18px;
    overflow: hidden;
    box-shadow: 0 14px 30px rgba(0,0,0,0.45);
  }

  /* Quillmarsh side */
  .card--quillmarsh { left: 90px; top: 170px; background: var(--quill-gray); }
  .quill-mark {
    position: absolute; left: 0; right: 0; top: 140px;
    text-align: center;
    font-family: "Marcellus", serif;
    font-size: 64px; letter-spacing: 3px;
    color: var(--paper);
  }

  /* Brindlecraft side */
  .card--brindlecraft { left: 490px; top: 610px; background: var(--paper); }
  .brand { position: absolute; left: 20px; width: 400px; top: 26px; text-align: center; }
  .brand__dot {
    width: 50px; height: 50px; border-radius: 50%;
    background: var(--teal); margin: 0 auto 12px;
  }
  .brand__name {
    font-family: "Marcellus", serif;
    font-size: 42px; letter-spacing: 2px; color: var(--navy); line-height: 1;
  }
  .brand__url {
    font-family: "Marcellus", serif;
    font-size: 15px; color: var(--navy); margin-top: 8px; letter-spacing: 0.5px;
  }

  .person { position: absolute; left: 60px; top: 214px; }
  .person__name { font-family: "Marcellus", serif; font-size: 26px; color: var(--navy); letter-spacing: 1px; }
  .person__title { font-size: 12px; font-weight: 600; color: var(--navy); margin-top: 2px; padding-left: 40px; }

  .divider {
    position: absolute; left: 318px; top: 180px; width: 2px; height: 110px;
    background: linear-gradient(to bottom, transparent, var(--rule), transparent);
  }

  .contact { position: absolute; left: 336px; top: 178px; list-style: none; }
  .contact li { display: flex; align-items: center; font-size: 16px; color: var(--navy); line-height: 30px; white-space: nowrap; }
  .contact svg { width: 13px; height: 13px; margin-right: 9px; fill: var(--teal); flex: none; }

  .address-band {
    position: absolute; left: 0; right: 0; bottom: 0; height: 58px;
    background: var(--navy);
    display: flex; align-items: center; justify-content: flex-end; padding-right: 36px;
    font-family: "Open Sans", sans-serif; font-size: 14px; color: var(--paper); letter-spacing: 0.3px;
  }
</style>
</head>
<body>

  <section class="card card--quillmarsh" aria-label="Quillmarsh side">
    <div class="quill-mark">QUILLMARSH</div>
  </section>

  <section class="card card--brindlecraft" aria-label="Brindlecraft side">
    <div class="brand">
      <div class="brand__dot"></div>
      <div class="brand__name">BRINDLECRAFT</div>
      <div class="brand__url">www.brindlecraft.com</div>
    </div>

    <div class="person">
      <div class="person__name">DANA HOLLOWAY</div>
      <div class="person__title">Graphics/ Photography Director</div>
    </div>

    <div class="divider"></div>

    <ul class="contact">
      <li>
        <svg viewBox="0 0 24 24"><path d="M6.6 10.8a15 15 0 0 0 6.6 6.6l2.2-2.2a1 1 0 0 1 1-.25 11.4 11.4 0 0 0 3.6.57 1 1 0 0 1 1 1V20a1 1 0 0 1-1 1A17 17 0 0 1 3 4a1 1 0 0 1 1-1h3.5a1 1 0 0 1 1 1c0 1.250.2 2.450.57 3.6a1 1 0 0 1-.25 1z"/></svg>
        555.201.7734
      </li>
      <li>
        <svg viewBox="0 0 24 24"><path d="M6 2h12v6H6zM3 9h18a1 1 0 0 1 1 1v7h-4v5H6v-5H2v-7a1 1 0 0 1 1-1zm5 8v3h8v-3z"/></svg>
        555.201.7790
      </li>
      <li>
        <svg viewBox="0 0 24 24"><path d="M2 5h20v14H2zm2 2v.5l8 5 8-5V7z"/></svg>
        dholloway@brindlecraft.com
      </li>
    </ul>

    <div class="address-band">PO Box 214/1180 Alder Creek Rd Fernvale, Virginia 24150</div>
  </section>

</body>
</html>
```